Cosmetic injections clinic needs a fresh looking business card

We need a business card using the supplied logo and color scheme to attract future clients to our clinic. It should be modern and fresh, eye catching and not too busy. Simple and to the point is best. I would like two sided designs with the front indicating address and contact information, and the back in full color with white logo and descriptive information also provided.
Target Market(s)
Clients looking for non surgical beauty enhancements.
Contact Information for Business Card
Lumivela
14, 415 Carrow Ridge Road
Fernwick, Ontario
K2P 7W3
Phone: 431-662-0974
Email: info@lumivela-example.com
Requirements
Must have
- -Logo supplied with the name and address of the clinic
- -Back of card in full color with white logo with A small line of text indicating both of the following: Anti aging consultants and cosmetic injectables
- Located inside the Wayfarer Care Group

```html
<!DOCTYPE html>
<html lang="en">
<head>
<meta charset="utf-8">
<title>Lumivela – Business Card</title>
<link href="https://fonts.googleapis.com/css2?family=Lato:wght@400;700&display=swap" rel="stylesheet">
<style>
  :root {
    --stage: #e9e6e4;
    --card-white: #ffffff;
    --ink: #2e2e33;
    --pink: #d6409a;
    --purple: #6f3fa3;
    --grad-top: #d8409a;
    --grad-bottom: #7a46a8;
    --on-color: #ffffff;
  }
  * { box-sizing: border-box; margin: 0; padding: 0; }
  html, body {
    width: 1200px; height: 844px; overflow: hidden;
    background: var(--stage);
    font-family: "Lato", Arial, sans-serif;
  }
  .stage {
    position: relative; width: 1200px; height: 844px;
    display: flex; align-items: center; justify-content: center; gap: 50px;
  }
  .card {
    position: relative; width: 525px; height: 300px;
    border-radius: 2px;
    box-shadow: 0 6px 18px rgba(0,0,0,0.18);
    overflow: hidden;
  }
  .brand { display: flex; align-items: center; gap: 12px; }
  .brand__dot { width: 46px; height: 46px; border-radius: 50%; background: var(--purple); flex: none; }
  .brand__name { font-size: 32px; font-weight: 700; letter-spacing: 0.5px; white-space: nowrap; }

  /* Front side */
  .card--front { background: var(--card-white); color: var(--ink); }
  .card--front .brand { position: absolute; top: 58px; right: 44px; }
  .card--front .brand__name { color: var(--purple); }
  .contact {
    position: absolute; left: 34px; right: 20px; bottom: 30px;
    font-size: 15px; line-height: 1.45;
  }
  .contact__row { display: flex; align-items: center; gap: 8px; }
  .contact__icon { width: 13px; height: 13px; flex: none; }
  .contact__name { margin-top: 8px; color: var(--purple); font-size: 17px; letter-spacing: 0.5px; }
  .contact__address { font-size: 15px; white-space: nowrap; }

  /* Back side */
  .card--back {
    background: linear-gradient(170deg, var(--grad-top) 0%, var(--grad-bottom) 100%);
    color: var(--on-color);
  }
  .card--back .brand { position: absolute; top: 62px; left: 50%; transform: translateX(-50%); }
  .card--back .brand__dot { background: var(--on-color); width: 54px; height: 54px; }
  .card--back .brand__name { color: var(--on-color); font-size: 38px; }
  .divider {
    position: absolute; left: 60px; right: 60px; top: 176px;
    height: 1px; background: rgba(255,255,255,0.45);
  }
  .tagline {
    position: absolute; left: 0; right: 0; top: 196px;
    text-align: center; font-size: 13px; letter-spacing: 0.8px;
    line-height: 1.9; text-transform: uppercase;
  }
</style>
</head>
<body>
  <main class="stage">
    <section class="card card--front" aria-label="Card front">
      <div class="brand">
        <span class="brand__dot"></span>
        <span class="brand__name">Lumivela</span>
      </div>
      <div class="contact">
        <div class="contact__row">
          <svg class="contact__icon" viewBox="0 0 16 16" aria-hidden="true">
            <path fill="#d6409a" d="M3.6 1.2l2.4 2.8-1.3 1.9c.8 1.9 2.4 3.6 4.4 4.5l1.9-1.3 2.8 2.4-1.4 2.6C7 14 2 9 1 3z"/>
          </svg>
          <span>431-662-0974</span>
        </div>
        <div class="contact__row">
          <svg class="contact__icon" viewBox="0 0 16 16" aria-hidden="true">
            <rect x="1" y="3" width="14" height="10" rx="1" fill="#d6409a"/>
            <path d="M1.5 4l6.5 5 6.5-5" fill="none" stroke="#fff" stroke-width="1.3"/>
          </svg>
          <span>info@lumivela-example.com</span>
        </div>
        <div class="contact__name">LUMIVELA</div>
        <div class="contact__address">14, 415 Carrow Ridge Road Fernwick, Ontario K2P 7W3</div>
      </div>
    </section>

    <section class="card card--back" aria-label="Card back">
      <div class="brand">
        <span class="brand__dot"></span>
        <span class="brand__name">Lumivela</span>
      </div>
      <div class="divider"></div>
      <p class="tagline">
        Anti aging consultants and cosmetic injectables<br>
        Located inside the Wayfarer Care Group
      </p>
    </section>
  </main>
</body>
</html>
```